Business cards for investing fund

I need processional luxury classical business cards for CEO of the investing company. I need it to be elegant. I need it to look expensive. It will be printed o fine paper with UV. I prefer light and minimalistic design. Logo of my company must be included at least on front page.

Target Market(s)

40+ investors

Industry/Entity Type

Finance And Accounting

Contact Information for Business Card

FRONT PAGE:

Wiktor Osmalek
President & CEO

e: vik@brlcap.example
w: www.brlcap.example
p: +44 20 7395 2847
m: +44 75 2918 3406

Brass Lark Venture Capital, LLC
17 W Pinecrest Ave., Sheridan, WY 82801
Filling number: 2019-000542319

BACK PAGE (with or without logo):

PROUD GROUP MEMBERS:

UK: Marrow Bay Associates Ltd. | 42 Elmsworth Row, 1st fl. | W1T-4QR London
PL: Marrow Bay Trust S.A. | ul. Lipowa Polna 14, 4p. | 00-871 Warszawa
US: Crestfall Advisors, LLC | 213 Orchard Lane, Suite 409, NYC | 10017 New York

Font styles to use
Serif
Sans Serif
Decorative

Colors
0355a3
ec1f27

Requirements
Must have
• My own logo (attached)

```html
<!DOCTYPE html>
<html lang="en">
<head>
<meta charset="utf-8">
<title>Brass Lark Venture Capital – Business Cards</title>
<link href="https://fonts.googleapis.com/css2?family=EB+Garamond:wght@400;600;700&display=swap" rel="stylesheet">
<style>
  :root {
    --bg: #e9eaec;
    --paper: #fbfbfa;
    --brand-blue: #0b4f9c;
    --ink: #4a4a4a;
    --rule: #555555;
  }
  * { margin: 0; padding: 0; box-sizing: border-box; }
  html, body { width: 1200px; height: 1069px; overflow: hidden; }
  body {
    background: var(--bg);
    font-family: "EB Garamond", Georgia, serif;
    color: var(--ink);
    position: relative;
  }
  .card {
    position: absolute;
    left: 250px;
    width: 700px;
    height: 400px;
    background: var(--paper);
    box-shadow: 0 10px 30px rgba(0,0,0,0.12);
  }
  .card--back { top: 100px; }
  .card--front { top: 570px; }

  /* back side */
  .brand-name {
    position: absolute;
    left: 60px;
    top: 178px;
    width: 270px;
    display: flex;
    align-items: center;
    gap: 12px;
    color: var(--brand-blue);
    font-weight: 600;
    font-size: 24px;
    line-height: 1.15;
  }
  .brand-name__mark {
    width: 14px;
    height: 14px;
    background: var(--brand-blue);
    flex: none;
  }
  .group-members {
    position: absolute;
    left: 360px;
    top: 62px;
    width: 310px;
    font-size: 15.5px;
    line-height: 1.2;
  }
  .group-members__title {
    color: var(--brand-blue);
    font-weight: 700;
    font-size: 15px;
    letter-spacing: 0.4px;
    margin-bottom: 6px;
  }
  .member { margin-bottom: 22px; padding-left: 12px; }
  .member__name { color: var(--brand-blue); font-weight: 700; }

  /* front side */
  .holder {
    position: absolute;
    left: 150px;
    top: 222px;
    width: 220px;
    text-align: right;
  }
  .holder__name {
    color: var(--brand-blue);
    font-weight: 700;
    font-size: 27px;
    line-height: 1.05;
  }
  .holder__title { font-size: 21px; line-height: 1.05; }
  .divider {
    position: absolute;
    left: 400px;
    top: 92px;
    width: 1.5px;
    height: 190px;
    background: var(--rule);
  }
  .contact {
    position: absolute;
    left: 430px;
    top: 86px;
    font-size: 17px;
    line-height: 1.25;
  }
  .contact__address { margin-bottom: 8px; }
  .contact__row { display: flex; align-items: center; gap: 10px; }
  .contact__row svg { width: 12px; height: 12px; fill: var(--brand-blue); flex: none; }
  .contact__filing { margin-top: 6px; }
</style>
</head>
<body>

<section class="card card--back" aria-label="Card back">
  <div class="brand-name">
    <span class="brand-name__mark" aria-hidden="true"></span>
    <span>Brass Lark Venture Capital LLC</span>
  </div>

  <div class="group-members">
    <p class="group-members__title">PROUD GROUP MEMBERS</p>
    <div class="member">
      <p class="member__name">UK: Marrow Bay Associates Ltd.</p>
      <p>42 Elmsworth Row, 1st fl.</p>
      <p>W1T-4QR London</p>
    </div>
    <div class="member">
      <p class="member__name">PL: Marrow Bay Trust S.A.</p>
      <p>ul. Lipowa Polna 14, 4p.</p>
      <p>00-871 Warszawa</p>
    </div>
    <div class="member">
      <p class="member__name">US: Crestfall Advisors, LLC</p>
      <p>213 Orchard Lane, Suite 409,</p>
      <p>NYC 10017 New York</p>
    </div>
  </div>
</section>

<section class="card card--front" aria-label="Card front">
  <div class="holder">
    <p class="holder__name">Wiktor Osmalek</p>
    <p class="holder__title">President &amp; CEO</p>
  </div>

  <div class="divider"></div>

  <div class="contact">
    <div class="contact__address">
      <p>LLC 17 W Pinecrest Ave.</p>
      <p>Sheridan, WY 82801</p>
    </div>
    <p class="contact__row">
      <svg viewBox="0 0 24 24" aria-hidden="true"><path d="M6.6 10.8a15 15 0 0 0 6.6 6.6l2.2-2.2a1 1 0 0 1 1-.25 11.4 11.4 0 0 0 3.6.57 1 1 0 0 1 1 1V20a1 1 0 0 1-1 1A17 17 0 0 1 3 4a1 1 0 0 1 1-1h3.5a1 1 0 0 1 1 1c0 1.25.2 2.45.57 3.57a1 1 0 0 1-.25 1z"/></svg>
      +44 20 7395 2847
    </p>
    <p class="contact__row">
      <svg viewBox="0 0 24 24" aria-hidden="true"><path d="M7 1h10a2 2 0 0 1 2 2v18a2 2 0 0 1-2 2H7a2 2 0 0 1-2-2V3a2 2 0 0 1 2-2zm0 3v14h10V4zm5 15.5a1.2 1.2 0 1 0 0 2.4 1.2 1.2 0 0 0 0-2.4z"/></svg>
      +44 75 2918 3406
    </p>
    <p class="contact__row">
      <svg viewBox="0 0 24 24" aria-hidden="true"><path d="M2 5h20v14H2zm2 2v.5l8 5 8-5V7l-8 5z"/></svg>
      vik@brlcap.example
    </p>
    <p class="contact__row">
      <svg viewBox="0 0 24 24" aria-hidden="true"><circle cx="12" cy="12" r="10"/></svg>
      www.brlcap.example
    </p>
    <p class="contact__filing">Filling number: 2019-000542319</p>
  </div>
</section>

</body>
</html>
```